Event branding Sales presentation PowerPoint template required

We are looking to freshen up & step up the professional quality of our powerpoint presentation template. I am looking for a professional designer with good creative background to design a new template for our presentations to new clients and for bespoke projects.
We have attached our current PPP as well as an elevator pitch which has most of the information we would like on the template

We have 3 main parts of our business which are:
- Event Branding
- Fan Engagements
- Set builds / Theming

Target Market(s)

Event organisers and sporting fedrations

Industry/Entity Type

Events

Requirements
Must have
• Ability for easy editing. Strong visual representation
Nice to have
• Information pages as well as look-book pages
Should not have
• Overcrowded graphics / arty graphics

```html
<!DOCTYPE html>
<html lang="en">
<head>
<meta charset="utf-8">
<title>Summit Events – Every Step of Your Event</title>
<link rel="stylesheet" href="https://fonts.googleapis.com/css2?family=Raleway:wght@500;700;800&family=Bebas+Neue&display=swap">
<style>
  :root {
    --frame: #050505;
    --slide: #404040;
    --white: #ffffff;
    --gold: #c9b68e;
    --gold-light: #dccaa6;
    --gold-icon: #e3c88a;
    --label: #8c8c8c;
  }
  * { margin: 0; padding: 0; box-sizing: border-box; }
  html, body { width: 1200px; height: 675px; overflow: hidden; background: var(--frame); }
  .slide {
    position: absolute; left: 7px; top: 7px; width: 1186px; height: 661px;
    background: var(--slide); overflow: hidden;
    font-family: "Raleway", sans-serif;
  }
  .slide-tab {
    position: absolute; left: 505px; top: -7px; width: 176px; height: 19px;
    background: var(--frame); border-radius: 0 0 6px 6px;
    display: flex; justify-content: center; align-items: center; gap: 6px;
  }
  .slide-tab span { width: 6px; height: 6px; border-radius: 50%; background: #555; }
  .nav { position: absolute; top: 36px; left: 0; }
  .nav a {
    position: absolute; white-space: nowrap; color: var(--white);
    font-size: 12px; font-weight: 700; text-decoration: none;
  }
  .nav .caret {
    display: inline-block; width: 0; height: 0; margin-left: 6px; vertical-align: 1px;
    border-left: 5px solid transparent; border-right: 5px solid transparent;
    border-top: 7px solid var(--gold-icon);
  }
  .brand {
    position: absolute; left: 986px; top: 33px; color: var(--gold);
    font-size: 15px; font-weight: 500; letter-spacing: 1.8px;
  }
  .flare {
    position: absolute; top: 234px; height: 40px;
    background: radial-gradient(ellipse at center, rgba(255,255,255,0.95) 0%, rgba(230,215,180,0.6) 6%, rgba(200,180,140,0.2) 28%, rgba(0,0,0,0) 70%);
  }
  .flare-left { left: -110px; width: 520px; }
  .flare-right { left: 780px; width: 520px; }
  .headline {
    position: absolute; left: 0; top: 199px; width: 1186px; text-align: center;
    color: var(--gold-light); font-size: 26px; font-weight: 800;
    letter-spacing: 6.4px; line-height: 30px; text-transform: uppercase;
    text-shadow: 1px 2px 3px rgba(0,0,0,0.6);
  }
  .steps { position: absolute; left: 0; top: 0; }
  .step-label {
    position: absolute; transform: translateX(-50%); text-align: center; white-space: nowrap;
    font-family: "Bebas Neue", sans-serif; font-size: 16px; line-height: 18px;
    letter-spacing: 3.2px; color: var(--label);
  }
  .pager { position: absolute; left: 575px; top: 636px; display: flex; gap: 6px; }
  .pager span { width: 7px; height: 7px; border-radius: 50%; background: var(--gold-icon); }
  .social { position: absolute; left: 1025px; top: 622px; display: flex; gap: 10px; }
  .social span {
    width: 22px; height: 22px; border-radius: 50%; background: var(--gold-icon);
    display: flex; align-items: center; justify-content: center;
  }
</style>
</head>
<body>
<main class="slide">
  <div class="slide-tab"><span></span><span></span><span></span></div>

  <nav class="nav">
    <a href="#" style="left:41px">HOME</a>
    <a href="#" style="left:140px">ABOUT US<i class="caret"></i></a>
    <a href="#" style="left:265px">SERVICES</a>
    <a href="#" style="left:386px">WHY SUMMIT EVENTS</a>
  </nav>
  <div class="brand">SUMMIT EVENTS</div>

  <div class="flare flare-left"></div>
  <div class="flare flare-right"></div>

  <h1 class="headline">Summit Events can assist through<br>every step<br>of your event</h1>

  <svg class="steps" width="1186" height="661">
    <defs>
      <linearGradient id="dusk" x1="0" y1="0" x2="0" y2="1">
        <stop offset="0" stop-color="#7c8ea6"/><stop offset="0.35" stop-color="#e9a46c"/>
        <stop offset="0.55" stop-color="#8a6d5e"/><stop offset="1" stop-color="#2c2a2c"/>
      </linearGradient>
      <linearGradient id="sea" x1="0" y1="0" x2="0" y2="1">
        <stop offset="0" stop-color="#8cc2e0"/><stop offset="0.45" stop-color="#4a9cc4"/>
        <stop offset="1" stop-color="#0f5f8c"/>
      </linearGradient>
      <linearGradient id="blend" x1="0" y1="0" x2="0" y2="1">
        <stop offset="0" stop-color="#9fb6cc"/><stop offset="0.4" stop-color="#f0c5a0"/>
        <stop offset="0.6" stop-color="#7aa8c4"/><stop offset="1" stop-color="#2f6f96"/>
      </linearGradient>
    </defs>
    <g transform="translate(-7,-4)">
      <g role="img" aria-label="Sunset over a shoreline, first view of the coastal panorama">
        <path d="M244 391 C280 392 296 420 290 452 C284 488 252 505 222 492 C196 481 186 452 194 424 C200 403 220 391 244 391Z" fill="url(#dusk)"/>
      </g>
      <g role="img" aria-label="Coastal panorama at sunset with a bridge deck">
        <path d="M350 392 C390 398 412 430 398 468 C386 498 350 508 326 488 C303 470 298 440 310 418 C320 400 334 390 350 392Z" fill="url(#dusk)"/>
      </g>
      <g role="img" aria-label="Bridge spanning calm water at dusk">
        <path d="M478 386 C510 388 526 412 514 440 C506 460 512 488 488 500 C460 512 432 496 424 466 C416 432 440 384 478 386Z" fill="url(#blend)"/>
      </g>
      <g role="img" aria-label="Long bridge over blue sea at dawn">
        <path d="M598 381 C638 384 660 414 650 452 C640 490 604 512 566 500 C536 490 524 464 534 438 C548 400 566 379 598 381Z" fill="url(#sea)"/>
      </g>
      <g role="img" aria-label="Bridge pier rising from blue water">
        <path d="M740 384 C768 390 772 430 760 460 C748 492 716 504 690 492 C660 478 656 448 676 424 C696 402 716 380 740 384Z" fill="url(#sea)"/>
      </g>
      <g role="img" aria-label="Lit bridge arches reflected on the sea">
        <path d="M855 382 C880 386 888 420 880 456 C872 490 842 508 812 496 C782 484 776 458 790 430 C806 398 830 378 855 382Z" fill="url(#sea)"/>
      </g>
      <g role="img" aria-label="Open blue sea meeting the horizon">
        <path d="M964 386 C994 392 1004 420 992 448 C982 470 990 494 962 504 C932 514 906 494 900 462 C894 426 926 380 964 386Z" fill="url(#sea)"/>
      </g>
    </g>
  </svg>

  <div class="step-label" style="left:239px;top:349px">Concept</div>
  <div class="step-label" style="left:465px;top:350px">Design</div>
  <div class="step-label" style="left:723px;top:333px">International<br>Logistics</div>
  <div class="step-label" style="left:953px;top:333px">Full Project<br>Management</div>
  <div class="step-label" style="left:349px;top:516px">Survey &amp;<br>Proposal</div>
  <div class="step-label" style="left:587px;top:516px">Build / Print</div>
  <div class="step-label" style="left:836px;top:516px">Installation<br>&amp; Rigging</div>

  <div class="pager"><span></span><span></span><span></span></div>

  <div class="social" aria-label="Contact links">
    <span aria-label="Social profile"></span>
    <span aria-label="Social profile"></span>
    <span aria-label="Social profile"></span>
    <span aria-label="Email">
      <svg width="12" height="9" viewBox="0 0 12 9" aria-hidden="true">
        <rect x="0.5" y="0.5" width="11" height="8" rx="1" fill="#404040"/>
        <path d="M1 1 L6 5 L11 1" fill="none" stroke="var(--gold-icon)" stroke-width="1"/>
      </svg>
    </span>
  </div>
</main>
</body>
</html>
```